Lorna Pettibone Nook Charmer

a larger business card may standard size 4” x 9” describing what I do. I don’t know if this would be considered a flyer. I rearrange, redesign and stage houses for the owner or to sell.

```html
<!DOCTYPE html>
<html lang="en">
<head>
<meta charset="utf-8">
<title>Lorna Pettibone – Nook Charmer</title>
<link rel="stylesheet" href="https://fonts.googleapis.com/css2?family=Montserrat:wght@400;500;600&family=Roboto:wght@400;700&display=swap">
<style>
  :root {
    --backdrop: #000000;
    --card: #ffffff;
    --ink: #111111;
    --teal: #3a9a94;
    --teal-dark: #1f5f5a;
    --sky: #63c7c1;
    --adobe: #e07a45;
    --adobe-deep: #a9532c;
    --mountain: #9b7a66;
    --patio: #d9b39a;
    --pool: #3aa6c9;
  }
  * { margin: 0; padding: 0; box-sizing: border-box; }
  html, body {
    width: 900px; height: 1200px; overflow: hidden;
    background: var(--backdrop);
  }
  .canvas { position: relative; width: 900px; height: 1200px; }

  .card {
    position: absolute; top: 127px; width: 420px; height: 945px;
    background: var(--card); overflow: hidden; color: var(--ink);
  }
  .card--front { left: 25px; }
  .card--back { left: 456px; }

  .line {
    position: absolute; left: 0; width: 100%;
    text-align: center; white-space: nowrap;
  }

  /* front */
  .hero-photo {
    position: absolute; left: 0; top: 0; width: 420px; height: 371px;
    background: linear-gradient(180deg, var(--sky) 0%, #8fd0c6 38%, var(--mountain) 48%, var(--adobe) 56%, var(--adobe) 78%, #c98f6a 90%, var(--patio) 100%);
  }
  .portrait {
    position: absolute; left: 135px; top: 296px; width: 148px; height: 148px;
    border-radius: 50%; border: 6px solid var(--card);
    background: radial-gradient(circle at 50% 40%, #d9c9c2 0%, #b8a8a4 45%, #6f8f5a 100%);
  }
  .name-front {
    top: 460px; font: 600 31px/1 "Montserrat", sans-serif; letter-spacing: 0.5px;
  }
  .title-front {
    top: 500px; font: 400 19px/1 "Montserrat", sans-serif; color: var(--teal); letter-spacing: 0.3px;
  }
  .services-head { top: 577px; font: 600 20px/1 "Montserrat", sans-serif; }
  .services {
    top: 605px; font: 400 18px/1 "Montserrat", sans-serif;
  }
  .services .dot { color: var(--teal-dark); font-size: 13px; padding: 0 6px; vertical-align: 2px; }
  .services-note {
    top: 632px; font: 400 15px/20px "Roboto", sans-serif; color: var(--teal);
  }
  .divider {
    position: absolute; left: 202px; top: 704px; width: 14px; height: 2px; background: var(--ink);
  }
  .contact {
    top: 740px; font: 400 17.5px/26.5px "Montserrat", sans-serif;
  }

  /* back */
  .name-back { top: 69px; font: 600 25px/1 "Montserrat", sans-serif; letter-spacing: 0.5px; }
  .title-back { top: 98px; font: 400 17px/1 "Montserrat", sans-serif; color: var(--teal); }
  .body {
    font: 400 15px/24px "Roboto", sans-serif;
  }
  .accent { color: var(--teal); }
  .b1 { top: 140px; }
  .b2 { top: 222px; line-height: 31px; }
  .b3 { top: 310px; }
  .b4 { top: 386px; }
  .b5 { top: 476px; font-size: 14px; }
  .b6 { top: 503px; }
  .b7 { top: 558px; }
  .b7 strong { font-weight: 700; }
  .patio-photo {
    position: absolute; left: 0; top: 688px; width: 420px; height: 257px;
    background:
      linear-gradient(180deg, var(--card) 0%, rgba(255,255,255,0) 10%),
      linear-gradient(180deg, #6b4a35 10%, #c46a45 28%, #8cc3d8 40%, var(--pool) 62%, var(--patio) 74%, #c9a58e 100%);
  }
</style>
</head>
<body>
<div class="canvas">

  <section class="card card--front">
    <div class="hero-photo" role="img" aria-label="Orange adobe house with wooden garage doors under a teal sky and desert mountains"></div>
    <div class="portrait" role="img" aria-label="Portrait photo of Lorna Pettibone"></div>
    <h1 class="line name-front">LORNA PETTIBONE</h1>
    <p class="line title-front">Nook Charmer</p>
    <h2 class="line services-head">HOMES</h2>
    <p class="line services">re-arrange<span class="dot">●</span>re-think<span class="dot">●</span>stage to sell</p>
    <p class="line services-note">With little or no cost, Lorna breathes new life<br>&amp; energy into your home</p>
    <div class="divider"></div>
    <p class="line contact">lornapettibone@fernmail.net<br>503-555-0148<br>4410 W. Marigold Lane. Dunmore, AZ 85300</p>
  </section>

  <section class="card card--back">
    <h2 class="line name-back">LORNA PETTIBONE</h2>
    <p class="line title-back">Nook Charmer</p>
    <p class="line body b1">For 36 years, Lorna was a real estate Broker in Oregon.<br>She has a track record of transforming houses<br>that do not sell, into homes that sell quickly.</p>
    <p class="line body b2 accent">As a Hearth &amp; Garden Living national award winner,<br>her talent has not gone unnoticed.</p>
    <p class="line body b3">She eagerly finds renewed energy by<br>re-arranging with what you have &amp; re-thinking your space.</p>
    <p class="line body b4">With a dash of this, a zest of that,<br>she re-invigorates your environment.</p>
    <p class="line body b5">Thrilled customers say...</p>
    <p class="line body b6 accent">“This is just how I dreamed my home would look!”</p>
    <p class="line body b7">Make your space livable, lovable and <strong>profitable...</strong><br>...a place where you, or your buyer, can hardly wait to<br>come home to...<br><strong>Voila!</strong></p>
    <div class="patio-photo" role="img" aria-label="Adobe courtyard patio with hammocks, pergola and a blue pool against desert mountains"></div>
  </section>

</div>
</body>
</html>
```